Flyer-Design für Grosshandelsunternehmen für Papeterie- und Bürobedarf
Zielgruppe
KOLDIG ist ein Schweizer Grosshandelsunternehmen für Papeterie- und Bürobedarf. Kunden sind ausschliesslich professionelle Wiederverkäufer. Endverbraucher werden nicht direkt, sondern über KOLDIG Kunden beliefert.
Das Sortiment umfasst neben Papeterie- und Schulartikeln eine kompetente Auswahl im Bereich Bürobedarf. Die Produktepalette wird laufend weiterentwickelt und umfasst auch den Bereich Catering & Kaffee, Hygiene & Reinigung sowie Betriebssicherheit – alles was im modernen Büro benötigt wird.
KOLDIG bietet seinen Kunden umfassende Dienstleistungen an. Diese ermöglichen es, das vom Markt geforderte breite und tiefe Sortiment zielgruppengerecht erfolgreich zu vermarkten und effizient zu verteilen. In enger Zusammenarbeit mit unseren Kunden und Lieferanten entwickeln wir unsere Dienstleistungen stetig weiter. Neben den Vermarktungszielen stehen Effizienzziele, die Doppelspurigkeiten in der Wertschöpfungskette vermeiden, im Vordergrund.
Das oberste Ziel von KOLDIG ist es, ein zuverlässiger Partner zu sein. Deshalb geniessen Servicegrad und Lieferqualität höchste Priorität. Wir streben nach kooperativen und langfristigen Geschäftsbeziehungen und setzen neue Technologien zum gemeinsamen Nutzen ein.
Aufgabenstellung
Erstellung eines 8-seitigen Layoutes, welches als Einleitung eines 600-seitigen Kataloges erscheint. Gemäss Briefing Vorlage, Dateiname Briefing_Trend_entwurfshalle.pdf. Texte können zu 100% übernommen werden und sollen in das von Ihnen vorgeschlagene Layout einfliessen, keine Änderungen vornehmen , nicht kürzen. Ihre Aufgabe besteht darin zum Text ein passendes Layout oder passende Grafiken zu erstellen. Wichtig; Die Bilder im Briefing sind als Anregung unsere Bildwelt Katalog gedacht, bitte integrieren Sie neue Bilder, welche zu Ihrem vorgeschlagenen Layout passen.
- InDesign Dokument
- Format 230 x 297 mm inkl. 3 mm Beschnitt
- Doppelseiten-Layout
- Anzahl Seiten 8
- Sprache deutsch
- Schrift vom Musterlayout übernehmen (ClanOT Schriftfamilie) keine anderen Schriften benützen, wichtig
- Grafische Elemente, wir benötigen am Ende die Originaldateien

```html
<!DOCTYPE html>
<html lang="de">
<head>
<meta charset="utf-8">
<title>Workplace Trend – Katalogeinleitung</title>
<link rel="stylesheet" href="https://fonts.googleapis.com/css2?family=Fira+Sans+Condensed:wght@300;400;600;700&display=swap">
<style>
:root{
  --bg:#cfcfcf;
  --paper:#ffffff;
  --blue:#6a8bc0;
  --blue-dark:#5577ad;
  --num:#dfe5f1;
  --grey-label:#8c8c8c;
  --ink:#3d3d3d;
  --body:#7a7a7a;
  --red:#d8473c;
}
*{margin:0;padding:0;box-sizing:border-box}
html,body{width:1200px;height:2644px;overflow:hidden;background:var(--bg)}
body{position:relative;font-family:"Fira Sans Condensed",sans-serif}
.page{position:absolute;background:var(--paper);overflow:hidden}
.spread{border-top:5px solid var(--blue)}
.single-top{border-top:5px solid var(--blue)}
.photo{position:absolute}
.footer{position:absolute;bottom:0;height:19px;background:var(--blue);color:#fff;font-weight:600;font-size:7.4px;letter-spacing:.15px;line-height:19px;padding-left:17px;white-space:nowrap}
.page-num{position:absolute;font-weight:700;font-size:80px;line-height:1;color:var(--num);letter-spacing:-2px}
.head{position:absolute;text-align:center;border-bottom:2px solid var(--blue);line-height:1}
.head .kicker{display:block;font-weight:300;font-size:21px;color:var(--ink);letter-spacing:.5px}
.head .title{display:block;font-weight:700;font-size:35px;color:var(--blue);letter-spacing:.3px;margin-top:1px}
.copy{position:absolute;font-weight:300;font-size:6.7px;line-height:10.2px;color:var(--body)}
.copy p+p{margin-top:10px}
.copy strong{font-weight:600;color:#555}
.tag{position:absolute;height:18px;line-height:18px;padding:0 7px;color:#fff;font-weight:600;font-size:11.5px;letter-spacing:.3px;white-space:nowrap}
.tag.blue{background:var(--blue)}
.tag.grey{background:var(--grey-label)}
.stat{position:absolute;width:80px;text-align:center}
.stat svg{display:block;margin:0 auto}
.stat p{font-weight:300;font-size:6.7px;line-height:10px;color:var(--body);margin-top:14px}
.cover-box{position:absolute;background:var(--blue);color:#fff;font-weight:700;font-size:18px;line-height:22px;text-align:center;letter-spacing:.3px;display:flex;align-items:center;justify-content:center}
</style>
</head>
<body>

<section class="page" style="left:411px;top:72px;width:333px;height:472px">
  <div class="photo" role="img" aria-label="Foto: Menschen eilen in Bewegungsunschärfe durch einen Büroflur" style="left:0;top:0;width:166px;height:172px;background:linear-gradient(160deg,#b79c7d,#7c6d62 55%,#4f5d7a)"></div>
  <div class="photo" role="img" aria-label="Foto: Kollegen mit Schutzmasken begrüssen sich mit dem Ellbogen" style="left:0;top:178px;width:166px;height:171px;background:linear-gradient(150deg,#e9ecef,#b9c0c7 60%,#5b6067)"></div>
  <div class="cover-box" style="left:172px;top:0;width:161px;height:67px">PAPETERIE- UND<br>BÜROBEDARF</div>
  <div class="photo" role="img" aria-label="Foto: zwei Kollegen betrachten lächelnd Unterlagen im Büro" style="left:172px;top:73px;width:161px;height:213px;background:linear-gradient(160deg,#e2e6ea,#a8b2bd 50%,#3e4f6e)"></div>
  <div class="head" style="left:190px;top:298px;width:143px">
    <span class="kicker">WORKPLACE</span>
    <span class="title" style="font-size:34px">TREND</span>
  </div>
  <div class="page-num" style="left:2px;top:392px;font-size:68px">01</div>
  <div class="copy" style="left:16px;top:364px;width:300px">
    <p>Als Experte für Büro-Bedarf und Büroausstattung bieten wir Ihnen ein umfassendes Produkt­sortiment für jeden Anwendungsbereich.</p>
    <p>Unsere Produkte unterstützen Sie bei der Einhaltung von Hygienekonzepten in den unterschied­lichsten Arbeitsbereichen, wobei wir unsere Schwerpunkte genauso auf die Datensicherheit Ihres Unternehmens oder die Ausstattung von Arbeitsplätzen legen.</p>
  </div>
  <div class="footer" style="left:0;width:333px">WIR LIEFERN INDIVIDUELL AUF IHRE ANFORDERUNGEN ABGESTIMMTE LÖSUNGEN.</div>
</section>

<section class="page spread" style="left:232px;top:594px;width:675px;height:478px">
  <div class="tag grey" style="left:0;top:26px">VERHINDERUNG VON</div>
  <div class="tag blue" style="left:0;top:50px">AUSBRÜCHEN</div>
  <div class="page-num" style="left:246px;top:14px">02</div>
  <div class="photo" role="img" aria-label="Foto: Menschen stehen verteilt auf einem hellen Netzwerk aus Linien" style="left:0;top:81px;width:338px;height:204px;background:linear-gradient(180deg,#f4f6f8,#dfe6ee 60%,#ffffff)"></div>
  <div class="head" style="left:16px;top:281px;width:208px;text-align:left">
    <span class="title">EINLEITUNG</span>
  </div>
  <div class="copy" style="left:16px;top:328px;width:306px">
    <p>Covid-19 beeinflusst aktuell, und mit hoher Wahrscheinlichkeit auch noch längere Zeit, Unternehmen aller Branchen. Unabhängig davon, ob es sich um einen Produktionsbetrieb, Büros, Ladengeschäfte oder Home-Office handelt.</p>
    <p>In jedem Bereich entstehen in dieser Situation neue Bedürfnisse, für die wir als kompetenter Partner die richtige Lösung liefern. Unsere Produkte unterstützen Sie effizient und wirksam im Bereich Social Distancing und realisieren Hygiene-Konzepte entsprechend der Vorgaben.</p>
    <p>Speziell für den Infektionsschutz entwickelte Produkte schützen Mitarbeiter am Arbeitsplatz und Ihre Kunden.</p>
  </div>
  <div class="footer" style="left:0;width:337px">WIR LIEFERN INDIVIDUELL AUF IHRE ANFORDERUNGEN ABGESTIMMTE LÖSUNGEN.</div>

  <div class="head" style="left:428px;top:24px;width:162px">
    <span class="kicker">BÜRO UND</span>
    <span class="title">BETRIEB</span>
  </div>
  <div class="page-num" style="left:592px;top:14px">03</div>
  <div class="copy" style="left:354px;top:98px;width:306px">
    <p>Die regelmässige Desinfektion der Hände und des Arbeitsplatzes ist eine wirksame Maßnahme, um das Infektionsrisiko nachweislich zu minimieren. Dies gilt vor allem für Büros mit Mobile Desk oder Desksharing. Hier ist die gründliche Oberflächenreinigung im Rahmen des Infektionsschutzes unverzichtbar. Aber auch nur von einer Person genutzte Schreibtische erfordern zuverlässige Hygiene. Unsere speziell für die Oberflächenreinigung entwickelten Desinfektions- und Reinigungsmittel stellen die Einhaltung der Vorgaben zum Infektionsschutz sicher.</p>
    <p>Ergänzend zu den desinfizierenden Maßnahmen bilden optisch attraktive Trennwände zusätzlichen Schutz, während Hinweisschilder in Meeting-Räumen die Besprechungs-Teilnehmer an die Vorgaben des Hygienekonzepts erinnern.</p>
    <p>Für den Empfangsbereich führen wir ein umfangreiches Produktsortiment von der Desinfektion, über Leitsysteme bis zu gut verständlichen Piktogrammen.</p>
  </div>
  <div class="photo" role="img" aria-label="Foto: Frau mit Maske desinfiziert einen Schreibtisch" style="left:337px;top:247px;width:203px;height:208px;background:linear-gradient(150deg,#c9ccd0,#8a9097 55%,#2d3034)"></div>
  <div class="photo" role="img" aria-label="Foto: Kollegen mit Masken im Grossraumbüro" style="left:547px;top:247px;width:128px;height:208px;background:linear-gradient(160deg,#dfe2e5,#9aa7b8 55%,#c98c3c)"></div>
  <div class="footer" style="left:338px;width:337px">WIR LIEFERN INDIVIDUELL AUF IHRE ANFORDERUNGEN ABGESTIMMTE LÖSUNGEN.</div>
</section>

<section class="page spread" style="left:232px;top:1109px;width:678px;height:478px">
  <div class="head" style="left:98px;top:24px;width:143px">
    <span class="kicker">BETRIEBS</span>
    <span class="title">BEDARF</span>
  </div>
  <div class="page-num" style="left:250px;top:14px">04</div>
  <div class="copy" style="left:16px;top:96px;width:306px">
    <p>Mit der Reinigung mit speziell auf das Hygienekonzept abgestimmten Reinigungsmitteln minimieren Sie die Virenbelastung von Oberflächen in allen Unternehmensbereichen und unterwegs auf Geschäfts­reise. Für zusätzliche Sicherheit sorgt ein ausreichend großer Abstand zu anderen Personen.</p>
    <p>Diesen erreichen Sie im Hotel, in der Gastro oder auf Messen durch Bodenmarkierungen und durch­dachte Leitsysteme. Schilder, Kleber und Tafeln bieten Platz für wichtige Hinweise und unterstützen die installierten Leitsysteme durch Zusatzinformationen.</p>
    <p>Absperrbänder verhindern das Betreten gesperrter Bereiche und Trennwände sorgen auf Messen, im Hotel und im Gastro-Bereich für Diskretion und zusätzlichen Schutz.</p>
  </div>
  <div class="photo" role="img" aria-label="Foto: Absperrpfosten und Bodenmarkierungen mit Fussabdrücken" style="left:0;top:221px;width:187px;height:236px;background:linear-gradient(160deg,#e8ecf2,#c2cbdc 55%,#7e8fb8)"></div>
  <div class="photo" role="img" aria-label="Foto: Bodenaufkleber mit Abstandshinweis auf grauem Boden" style="left:194px;top:221px;width:145px;height:236px;background:linear-gradient(160deg,#d8d8d8,#bdbdbd 60%,#9e9e9e)"></div>
  <div class="tag blue" style="left:262px;top:212px">AUFKLEBER</div>
  <div class="tag blue" style="left:246px;top:235px;border-bottom:2px solid var(--red);line-height:16px">SCHILDER UND</div>
  <div class="tag blue" style="left:284px;top:259px">TAFELN</div>
  <div class="footer" style="left:0;width:338px">WIR LIEFERN INDIVIDUELL AUF IHRE ANFORDERUNGEN ABGESTIMMTE LÖSUNGEN.</div>

  <div class="head" style="left:428px;top:24px;width:162px">
    <span class="kicker">WASCH</span>
    <span class="title">RAUM</span>
  </div>
  <div class="page-num" style="left:591px;top:14px">05</div>
  <div class="copy" style="left:356px;top:96px;width:306px">
    <p>Mit unserem umfangreichen Produktsortiment unterstützen wir Sie, die Hygienemaßnahmen in Wa­schräumen auf hohem Niveau umzusetzen.</p>
    <p>Speziell für die Oberflächendesinfektion entwickelte Produkte sorgen für bakterien- und keimfreie Sanitäranlagen, während schonende Reinigungsmittel die allgemeine Sauberkeit im Waschraum gewährleisten. Ein weiteres Thema ist das professionelle Waste-Management für die korrekte Ent­sorgung des vorhandenen Abfalls.</p>
    <p>Hier bilden geschlossene Abfalleimer eine wichtige Voraussetzung, um eine Belastung des Umfeldes mit Keimen und Viren zu minimieren.</p>
    <p>Denn wirksamer Infektionsschutz am Arbeitsplatz betrifft alle von Ihren Mitarbeitern genutzten Räume im Unternehmen.</p>
  </div>
  <div class="tag grey" style="left:358px;top:251px;width:300px;text-align:center">DIE QUALITÄT DER TOILETTEN AM ARBEITSPLATZ IST</div>
  <div class="tag blue" style="left:440px;top:277px">BESONDERS WICHTIG!</div>

  <div class="stat" style="left:364px;top:322px">
    <svg width="54" height="54" viewBox="0 0 54 54"><circle cx="27" cy="27" r="24" fill="none" stroke="#e3e8f2" stroke-width="3"/><circle cx="27" cy="27" r="24" fill="none" stroke="var(--blue)" stroke-width="3" stroke-dasharray="122 151" transform="rotate(-90 27 27)"/><text x="27" y="31" text-anchor="middle" font-family="Fira Sans Condensed,sans-serif" font-weight="600" font-size="11" fill="var(--blue)">81%</text></svg>
    <p>Eine ordentliche und gepflegte Toilette am Arbeits­platz zeugt von Fürsorge für die Mitarbeiter.</p>
  </div>
  <div class="stat" style="left:468px;top:322px">
    <svg width="54" height="54" viewBox="0 0 54 54"><circle cx="27" cy="27" r="24" fill="none" stroke="#e3e8f2" stroke-width="3"/><circle cx="27" cy="27" r="24" fill="none" stroke="var(--blue)" stroke-width="3" stroke-dasharray="121 151" transform="rotate(-90 27 27)"/><text x="27" y="31" text-anchor="middle" font-family="Fira Sans Condensed,sans-serif" font-weight="600" font-size="11" fill="var(--blue)">80%</text></svg>
    <p>Eine saubere Toilette verbessert das Gefühl des Wohlbefindens bei der Arbeit.</p>
  </div>
  <div class="stat" style="left:569px;top:322px">
    <svg width="54" height="54" viewBox="0 0 54 54"><circle cx="27" cy="27" r="24" fill="none" stroke="#e3e8f2" stroke-width="3"/><circle cx="27" cy="27" r="24" fill="none" stroke="var(--blue)" stroke-width="3" stroke-dasharray="137 151" transform="rotate(-90 27 27)"/><text x="27" y="31" text-anchor="middle" font-family="Fira Sans Condensed,sans-serif" font-weight="600" font-size="11" fill="var(--blue)">91%</text></svg>
    <p>Verfügbarkeit von Toilettenpapier ist ein Muss.</p>
  </div>
  <div class="footer" style="left:340px;width:338px">WIR LIEFERN INDIVIDUELL AUF IHRE ANFORDERUNGEN ABGESTIMMTE LÖSUNGEN.</div>
</section>

<section class="page spread" style="left:232px;top:1634px;width:684px;height:483px">
  <div class="head" style="left:89px;top:24px;width:162px">
    <span class="kicker">DATEN</span>
    <span class="title">SCHUTZ</span>
  </div>
  <div class="page-num" style="left:252px;top:14px">06</div>
  <div class="copy" style="left:16px;top:96px;width:306px">
    <p>Trotz eindeutiger gesetzlicher Vorgaben und einheitlicher Datenschutzstandards gehen viele Mit­arbeiter im Unternehmen noch nachlässig mit sensiblen Daten um.</p>
    <p>Die Folgen für das Unternehmen können gravierend sein und ziehen im Ernstfall hohe Strafen nach sich. Während der Zugriff auf digitale Daten aufgrund durchdachter Sicherheitsmaßnahmen für unbefugte Personen immer schwieriger wird, gelangen auf Papier gedruckte Daten durch den nachlässigen Umgang immer noch viel zu häufig in unbefugte Hände.</p>
    <p>Die Lösung sind spezielle Aktenvernichter, die Daten auf Papier so vernichten, dass je nach Sicher­heitsstufe eine Wiederherstellung unmöglich ist.</p>
    <p>Wir führen Aktenvernichter für unterschiedliche Sicherheitsstufen, die sensible Informationen zuverlässig vernichten. Mit leistungsfähigen Aktenvernichtern lässt sich das <strong>Datenleck Papierkorb</strong> vermeiden und sensible Daten können absolut sicher vor dem Zugriff Unbefugter entsorgt werden.</p>
    <p>Das Sicherheitsrisiko besteht genauso im privaten Umfeld, im Home-Office, sowie auch in Klein­unternehmen.</p>
  </div>
  <div class="photo" role="img" aria-label="Foto: leuchtendes Schloss-Symbol vor digitalem Hintergrund" style="left:0;top:319px;width:107px;height:143px;background:linear-gradient(150deg,#cfe3ea,#7fa6b6 55%,#3a5a6d)"></div>
  <div class="photo" role="img" aria-label="Foto: Hände blättern in gestapelten Akten" style="left:113px;top:319px;width:225px;height:143px;background:linear-gradient(160deg,#f1f2f4,#c9ccd4 55%,#4e5260)"></div>
  <div class="tag blue" style="left:76px;top:287px">MINIMIERTES</div>
  <div class="tag blue" style="left:60px;top:310px">SICHERHEITSRISIKO</div>
  <div class="footer" style="left:0;width:341px">WIR LIEFERN INDIVIDUELL AUF IHRE ANFORDERUNGEN ABGESTIMMTE LÖSUNGEN.</div>

  <div class="head" style="left:431px;top:24px;width:162px">
    <span class="kicker">HOME</span>
    <span class="title">OFFICE</span>
  </div>
  <div class="page-num" style="left:594px;top:14px">07</div>
  <div class="copy" style="left:359px;top:96px;width:306px">
    <p>Seit Beginn der Pandemie gingen viele Mitarbeiter in das Home-Office, und erledigen Ihre Arbeit von Zuhause aus.</p>
    <p>Obwohl eubstweilen ein Teil der Arbeitnehmer wieder zurück im Büro ist, entwickelte sich das Home-Office für andere aus einer vorerst temporären zur dauerhaften Lösung.</p>
    <p>Wie im Büro ist jedoch auch bei der Arbeit von Zuhause aus die Ergonomie des Arbeitsplatzes und seine professionelle Ausstattung vom PC bis zur <strong>Peripherie-Hardware für Print</strong> ein wichtiges Thema. In unserem umfangreichen Sortiment für Büroausstattung führen wir eine große Auswahl <strong>hochwertiger Produkte</strong> vom Büro-Stuhl über Bodenschutzmatten bis zu Tastatur und Maus. Ein Headset ist die Voraussetzung, um an einer Video Conference oder einem Webinar teilzunehmen.</p>
  </div>
  <div class="tag blue" style="left:358px;top:227px;width:184px">HOME-OFFICE AUSSTATTUNGEN</div>
  <div class="photo" role="img" aria-label="Foto: Videokonferenz auf einem Laptop am Schreibtisch" style="left:358px;top:245px;width:184px;height:217px;background:linear-gradient(160deg,#c99a67,#8a6a4e 50%,#2f3440)"></div>
  <div class="photo" role="img" aria-label="Foto: Frau arbeitet nachdenklich am Laptop in heller Wohnung" style="left:549px;top:227px;width:135px;height:235px;background:linear-gradient(160deg,#f2f0ec,#dcd6cc 55%,#c79a3f)"></div>
  <div class="footer" style="left:343px;width:341px">WIR LIEFERN INDIVIDUELL AUF IHRE ANFORDERUNGEN ABGESTIMMTE LÖSUNGEN.</div>
</section>

<section class="page single-top" style="left:430px;top:2148px;width:314px;height:446px">
  <div class="head" style="left:66px;top:22px;width:166px">
    <span class="kicker">NEUES KAPITEL</span>
    <span class="title">SCHULE</span>
  </div>
  <div class="page-num" style="left:232px;top:12px">08</div>
  <div class="copy" style="left:16px;top:92px;width:284px">
    <p>Wir haben unser bereits umfangreiches Produktsortiment an Schulbedarf mit den erforderlichen Unterrichtsmaterialien und Hilfsmitteln dem Lehrplan 21 angepasst.</p>
    <p>Dabei liegt der Schwerpunkt auf Unterrichtsmaterialien, die vor allem im kreativen Bereich ein­gesetzt werden. Hochwertige Farbstifte, Acryl-, Öl- und Aquarellfarben zählen dazu. Aber auch Kleister, Klebeband, Leim oder Gips sind ein Teil der Kreativmaterialien.</p>
    <p>Für den Zeichenunterricht benötigte Pinsel, Papier und Tusche finden Sie im Sortiment genauso wie Modellierer-Utensilien wie Spachtel, Schwamm sowie Modellier- und Schnittwerkzeug.</p>
    <p><strong>Lehrplan 21:</strong> Der Lehrplan legt fest, was Schülerinnen und Schüler in jedem Fachbereich und in jedem Zyklus lernen. Er ist eine Grundlage für die Entwicklung der Lehrmittel, ein Planungs­instrument für Lehrpersonen sowie für die Aus- und Weiterbildung der Lehrpersonen.</p>
  </div>
  <div class="photo" role="img" aria-label="Foto: Kinderhand schreibt Buchstaben in ein Heft" style="left:0;top:237px;width:119px;height:190px;background:linear-gradient(160deg,#e9a9b4,#f2dcd8 55%,#f7f1ee)"></div>
  <div class="photo" role="img" aria-label="Foto: zwei Schulkinder malen mit Farbstiften am Tisch" style="left:126px;top:237px;width:188px;height:190px;background:linear-gradient(160deg,#7d8f9c,#5b6a78 45%,#c7a06a)"></div>
  <div class="footer" style="left:0;width:314px">WIR LIEFERN INDIVIDUELL AUF IHRE ANFORDERUNGEN ABGESTIMMTE LÖSUNGEN.</div>
</section>

</body>
</html>
```